Stickers to put on my honeyglasses

Stickers for my honey glasses.
Only a single sticker on the front. Same should have a stripe on the top side which goes above the lid to show if the glass was opened.
Size of the main part should be 55mm high and max. 100 mm wide.
The stripe on the top should be 70mm long.
I added a Picture of another producer which uses the same glass as I do.
I should say: 'e Maringer Glas Hunneg'. which means 'another glass of honey. 'Hunneg' should be mainly visible and therefore very large. 'e Maringer Glas' should be less visible and therefore smaller above the 'Hunneg'
- It needs to contain the quantity : '500gr'
- It needs to contain my Name and address: 'Jos Maringer, 14, rue Pierre Faber, L-7590 Miersch' (This should be small and not to visible)
- It needs to conatin a validity Line: ´Am beschte virum:` (With enough space so I can add a date by hand)
- It needs to say: 'dréchen, kill andäischterstockéieren' (to store it dry cold and dark)

```html
<!DOCTYPE html>
<html lang="lb">
<head>
<meta charset="utf-8">
<title>Hunneg – Etikett mat Siegelstreif</title>
<link rel="stylesheet" href="https://fonts.googleapis.com/css2?family=Roboto+Condensed:wght@700&family=Righteous&family=Vollkorn:wght@600;700&display=swap">
<style>
  :root {
    --brown: #4a1f17;
    --orange: #f28c1f;
    --honey: #fdd38a;
    --leaf: #8f9a66;
    --cutline: #2a6f8f;
    --ink: #111111;
    --paper: #ffffff;
  }
  html, body {
    margin: 0;
    padding: 0;
    width: 1158px;
    height: 1200px;
    overflow: hidden;
    background: var(--paper);
  }
  .sheet { display: block; width: 1158px; height: 1200px; }
  .dimension-label {
    font-family: "Roboto Condensed", "Arial Narrow", sans-serif;
    font-weight: 700;
    fill: var(--ink);
  }
  .dimension-line { stroke: var(--ink); stroke-width: 1.4; fill: none; }
  .cut-line { stroke: var(--cutline); stroke-width: 1.6; stroke-dasharray: 6 5; fill: none; }
  .fold-line { stroke: var(--ink); stroke-width: 1.6; stroke-dasharray: 7 6; fill: none; }
  .brand-title { font-family: "Righteous", sans-serif; fill: var(--brown); }
  .serif { font-family: "Vollkorn", Georgia, serif; fill: var(--brown); }
  .tagline { font-weight: 700; letter-spacing: 2px; }
  .quantity { font-weight: 700; }
  .best-before { font-weight: 700; }
  .storage-note { font-weight: 700; letter-spacing: 1px; }
  .maker-address { font-weight: 600; }
  .rule { stroke: var(--orange); stroke-width: 2; }
</style>
</head>
<body>
<svg class="sheet" viewBox="0 0 1158 1200" xmlns="http://www.w3.org/2000/svg">
  <defs>
    <marker id="arrow" viewBox="0 0 10 10" refX="9" refY="5" markerWidth="8" markerHeight="8" orient="auto-start-reverse">
      <path d="M0 2 L10 5 L0 8 Z" fill="var(--ink)"/>
    </marker>
    <path id="tagline-arc" d="M548 735 Q677 680 806 735"/>
  </defs>

  <!-- Dimensions -->
  <g class="dimensions">
    <text class="dimension-label" x="591" y="103" font-size="44" text-anchor="middle">20 mm.</text>
    <line class="dimension-line" x1="524" y1="112" x2="524" y2="135"/>
    <line class="dimension-line" x1="657" y1="112" x2="657" y2="135"/>
    <line class="dimension-line" x1="525" y1="123" x2="656" y2="123" marker-start="url(#arrow)" marker-end="url(#arrow)"/>

    <line class="dimension-line" x1="100" y1="187" x2="124" y2="187"/>
    <line class="dimension-line" x1="100" y1="1024" x2="124" y2="1024"/>
    <line class="dimension-line" x1="112" y1="188" x2="112" y2="1023" marker-start="url(#arrow)" marker-end="url(#arrow)"/>
    <text class="dimension-label" font-size="48" text-anchor="middle" transform="translate(95 597) rotate(-90)">125 mm.</text>

    <line class="dimension-line" x1="170" y1="187" x2="194" y2="187"/>
    <line class="dimension-line" x1="170" y1="656" x2="194" y2="656"/>
    <line class="dimension-line" x1="170" y1="1024" x2="194" y2="1024"/>
    <line class="dimension-line" x1="182" y1="188" x2="182" y2="655" marker-start="url(#arrow)" marker-end="url(#arrow)"/>
    <line class="dimension-line" x1="182" y1="657" x2="182" y2="1023" marker-start="url(#arrow)" marker-end="url(#arrow)"/>
    <text class="dimension-label" font-size="32" text-anchor="middle" transform="translate(172 417) rotate(-90)">70 mm.</text>
    <text class="dimension-label" font-size="32" text-anchor="middle" transform="translate(172 833) rotate(-90)">55 mm.</text>

    <line class="dimension-line" x1="957" y1="656" x2="981" y2="656"/>
    <line class="dimension-line" x1="969" y1="188" x2="969" y2="474" marker-start="url(#arrow)" marker-end="url(#arrow)"/>
    <line class="dimension-line" x1="969" y1="476" x2="969" y2="655" marker-start="url(#arrow)" marker-end="url(#arrow)"/>
    <text class="dimension-label" font-size="32" text-anchor="middle" transform="translate(986 349) rotate(90)">43 mm.</text>
    <text class="dimension-label" font-size="32" text-anchor="middle" transform="translate(986 564) rotate(90)">27 mm.</text>

    <line class="dimension-line" x1="255" y1="1088" x2="255" y2="1112"/>
    <line class="dimension-line" x1="925" y1="1088" x2="925" y2="1112"/>
    <line class="dimension-line" x1="256" y1="1100" x2="924" y2="1100" marker-start="url(#arrow)" marker-end="url(#arrow)"/>
    <text class="dimension-label" x="612" y="1155" font-size="46" text-anchor="middle">100 mm.</text>

    <line class="fold-line" x1="674" y1="187" x2="980" y2="187"/>
    <line class="fold-line" x1="545" y1="475" x2="980" y2="475"/>
    <line class="dimension-line" x1="950" y1="656" x2="980" y2="656"/>
  </g>

  <!-- Cut outline -->
  <path class="cut-line" d="M524 656 V187 H657 V656 H876 A49 49 0 0 1 925 705 V975 A49 49 0 0 1 876 1024 H304 A49 49 0 0 1 255 975 V705 A49 49 0 0 1 304 656 Z"/>

  <!-- Seal strip -->
  <g class="seal-strip">
    <text class="serif tagline" font-size="17" text-anchor="middle" transform="translate(567 332) rotate(-90)">· · e Maringer Glas · ·</text>
    <text class="brand-title" font-size="58" text-anchor="middle" textLength="215" lengthAdjust="spacingAndGlyphs" transform="translate(623 323) rotate(-90)">HUNNEG</text>
    <rect x="550" y="492" width="82" height="194" rx="30" fill="var(--orange)" opacity="0.85" role="img" aria-label="Illustration: eine Biene fliegt auf einer gestrichelten Bahn zu einer orangen Blüte"/>
  </g>

  <!-- Main label -->
  <g class="main-label">
    <rect x="228" y="668" width="214" height="352" rx="40" fill="url(#floral-tone)" role="img" aria-label="Illustration: orange Blumen mit grünen Blättern, Honigwaben und eine Biene"/>
    <defs>
      <linearGradient id="floral-tone" x1="0" y1="0" x2="0" y2="1">
        <stop offset="0" stop-color="var(--orange)"/>
        <stop offset="0.5" stop-color="var(--honey)"/>
        <stop offset="1" stop-color="var(--leaf)"/>
      </linearGradient>
    </defs>

    <text class="serif tagline" font-size="24"><textPath href="#tagline-arc" startOffset="50%" text-anchor="middle">· · e Maringer Glas · ·</textPath></text>
    <line class="rule" x1="594" y1="742" x2="657" y2="742"/>
    <circle cx="677" cy="742" r="6" fill="none" stroke="var(--orange)" stroke-width="2"/>
    <line class="rule" x1="697" y1="742" x2="760" y2="742"/>

    <text class="brand-title" x="470" y="841" font-size="112" textLength="414" lengthAdjust="spacingAndGlyphs">HUNNEG</text>

    <line class="rule" x1="585" y1="864" x2="660" y2="864"/>
    <polygon points="677,853 687,858.5 687,869.5 677,875 667,869.5 667,858.5" fill="var(--orange)"/>
    <line class="rule" x1="694" y1="864" x2="769" y2="864"/>
    <text class="serif quantity" x="887" y="877" font-size="34" text-anchor="end">500gr</text>

    <text class="serif best-before" x="465" y="912" font-size="25">Am beschte virum:</text>
    <line class="rule" x1="452" y1="926" x2="901" y2="926"/>
    <text class="serif storage-note" x="456" y="953" font-size="17" textLength="432" lengthAdjust="spacing">DRÉCHEN, KILL AN DÄISCHTER STOCKÉIEREN'</text>
    <line class="rule" x1="452" y1="965" x2="901" y2="965"/>
    <text class="serif maker-address" x="676" y="993" font-size="15.5" text-anchor="middle">Jos Maringer  •  14, rue Pierre Faber  •  L-7590 Miersch</text>
  </g>
</svg>
</body>
</html>
```